VKTO Meridian LLC Website

Basic website for a start up business in the defense and federal space. If we could have intelligence analysis and technology as a focus that would be great. Looking to use our core colors but a lighter set of web pages would be preferable

Target Market(s)

Defense

Coding

Coded - Design and coding required

Number of Pages Required

3 page

```html
<!DOCTYPE html>
<html lang="en">
<head>
<meta charset="utf-8">
<title>VKTO Meridian LLC</title>
<link href="https://fonts.googleapis.com/css2?family=Montserrat:wght@400;500;600;700&family=Oswald:wght@400&display=swap" rel="stylesheet">
<style>
:root{
  --red:#b3132f;
  --red-dark:#640a1d;
  --pink:#d9788a;
  --navy:#14456c;
  --ink:#2b2b2b;
  --muted:#6b6b6b;
  --line:#d6d6d6;
  --footer:#1e1a1b;
  --white:#ffffff;
}
*{box-sizing:border-box;margin:0;padding:0}
html,body{width:1200px;height:3260px;overflow:hidden}
body{position:relative;font-family:'Montserrat',sans-serif;color:var(--ink);background:var(--white)}
.abs{position:absolute}
.btn{position:absolute;display:flex;align-items:center;justify-content:center;font-size:13px;font-weight:500;text-transform:uppercase;letter-spacing:.3px;color:var(--white);background:var(--red)}
.btn.outline{background:transparent;border:1.5px solid var(--white)}
.btn.light{background:var(--white);color:var(--red)}

/* hero */
.hero{position:absolute;left:0;top:0;width:1200px;height:680px}
.brand{position:absolute;left:161px;top:36px;font-size:30px;font-weight:600;color:var(--white);letter-spacing:2px;display:flex;align-items:center;gap:10px}
.brand .dot{width:14px;height:14px;border-radius:50%;background:var(--red)}
.nav{position:absolute;top:42px;font-size:13px;color:var(--white);text-transform:uppercase}
.nav.active{font-weight:700}
.hero-title{position:absolute;left:0;width:1200px;top:262px;text-align:center;font-family:'Oswald',sans-serif;font-size:45px;line-height:55px;color:var(--white)}

/* frames */
.frame{position:absolute;border:4px solid var(--red)}
.frame.soft{border-color:var(--pink)}
.photo{position:absolute}

.h2{position:absolute;font-size:33px;font-weight:600;color:var(--red);text-transform:uppercase;line-height:41px}
.lead{position:absolute;font-size:14.5px;line-height:27px;color:var(--red)}
.lead.grey{color:var(--muted)}
.body{position:absolute;font-size:12px;line-height:24.5px;color:var(--muted);letter-spacing:.3px}

.panel{position:absolute;top:1256px;width:600px;height:463px}
.panel h3{position:absolute;top:118px;font-size:31px;font-weight:500;color:var(--white);text-transform:uppercase}
.panel p{position:absolute;top:176px;width:385px;font-size:12.5px;line-height:24.5px;color:var(--white);letter-spacing:.5px}

.cta{position:absolute;left:0;top:2323px;width:1200px;height:374px}
.cta-text{position:absolute;left:0;width:1200px;top:2442px;text-align:center;font-size:25px;font-weight:500;line-height:35px;color:var(--white)}

.h4{position:absolute;top:2782px;font-size:20px;font-weight:700;color:var(--red);text-transform:uppercase}
.icon{position:absolute;width:52px;height:52px;border:1.5px solid var(--red);border-radius:50%;display:flex;align-items:center;justify-content:center}
.social{position:absolute;width:38px;height:38px;border:1.5px solid var(--red);border-radius:50%;top:3088px}
.info{position:absolute;left:228px;font-size:14px;line-height:21px;color:var(--ink)}
.info .label{color:var(--red);font-size:15px;font-weight:500;text-transform:uppercase}
.field{position:absolute;left:637px;width:402px;border:1px solid var(--line);font-size:12.5px;color:var(--ink);padding:0 16px;display:flex;align-items:center}
.field.area{align-items:flex-start;padding-top:12px}

.footer{position:absolute;left:0;top:3216px;width:1200px;height:44px;background:var(--footer);color:var(--white);font-size:12.5px}
.footer span{position:absolute;top:15px}
</style>
</head>
<body>

<!-- hero -->
<svg class="hero" viewBox="0 0 1200 680" role="img" aria-label="Photo of the Capitol building under a blue sky with a navy overlay">
  <defs>
    <linearGradient id="sky" x1="0" y1="0" x2="0" y2="1">
      <stop offset="0" stop-color="#0f3f66"/>
      <stop offset=".55" stop-color="#2f5f86"/>
      <stop offset="1" stop-color="#5d7d98"/>
    </linearGradient>
  </defs>
  <rect width="1200" height="680" fill="url(#sky)"/>
  <polygon points="0,540 600,672 1200,540 1200,680 0,680" fill="var(--red)"/>
  <polygon points="0,552 600,656 1200,552 1200,680 0,680" fill="var(--white)"/>
</svg>

<div class="brand"><span>VKTO MERIDIAN</span><span class="dot"></span></div>
<span class="nav active" style="left:656px">Home</span>
<span class="nav" style="left:724px">About Us</span>
<span class="nav" style="left:822px">Services</span>
<div class="btn" style="left:912px;top:30px;width:126px;height:40px">Contact Us</div>

<h1 class="hero-title">Creating Breakthrough Technologies And Capabilities<br>In Defence And Federal Space</h1>
<div class="btn" style="left:537px;top:390px;width:126px;height:40px">Contact Us</div>

<!-- about -->
<div class="frame soft" style="left:139px;top:744px;width:156px;height:146px;border-width:3px"></div>
<div class="frame" style="left:428px;top:1006px;width:168px;height:159px"></div>
<div class="photo" role="img" aria-label="Photo of two business people in a meeting at a wooden table" style="left:161px;top:766px;width:401px;height:373px;background:linear-gradient(135deg,#9c5a3c,#c48a4e 55%,#6a4a3a)"></div>

<h2 class="h2" style="left:651px;top:788px">About Us</h2>
<p class="lead" style="left:651px;top:840px;width:390px">Lorem ipsum dolor sit amet, consectetuer adipiscing elitgn sed diam nibh euismod tincidunt ut.</p>
<p class="body" style="left:651px;top:899px;width:390px">Lorem ipsum dolor sit amet, consectetuer adipiscing elit, sed diam nonummy nibh euismod tincidunt ut laoreet dolore magna aliquam erat volutat. Ut wisi enim ad minim veniam, quis nostrud exerci tation ullamcorper susipi lobortis nisl ut aliquip ex ea commodo consequat. Duis autem vel eum iriure dolor in hendrerit in vulputate velit esse.</p>
<div class="btn" style="left:651px;top:1067px;width:127px;height:41px">Read More</div>

<!-- panels -->
<div class="panel" role="img" aria-label="Photo of a soldier with digital overlay in red tones" style="left:0;background:radial-gradient(circle at 60% 30%,#e0506a,#b3203c 60%,#7e1428)">
  <h3 style="left:162px">Defence</h3>
  <p style="left:162px">Lorem ipsum dolor sit amet, consectetuer adipiscing elit sed nonumy nibh euismod tincidunt ut laoreet dolore magna volutat. Ut wisi enim ad minim veniam quis nostrud exerci tation.</p>
  <div class="btn outline" style="left:162px;top:294px;width:128px;height:41px">Read More</div>
</div>
<div class="panel" role="img" aria-label="Photo of a federal courthouse facade in dark tones" style="left:600px;background:linear-gradient(160deg,#3a3a3a,#555049 50%,#2a2826)">
  <h3 style="left:54px">Federal Space</h3>
  <p style="left:57px">Lorem ipsum dolor sit amet, consectetuer adipiscing elit sed nonumy nibh euismod tincidunt ut laoreet dolore magna volutat. Ut wisi enim ad minim veniam quis nostrud exerci tation.</p>
  <div class="btn outline" style="left:57px;top:294px;width:128px;height:41px">Read More</div>
</div>

<!-- intelligence -->
<h2 class="h2" style="left:161px;top:1833px">Intelligence Analysis<br>And Technology</h2>
<p class="lead grey" style="left:161px;top:1926px;width:390px">Lorem ipsum dolor sit amet, consectetuer adipiscing elitgn sed diam nibh euismod tincidunt ut.</p>
<p class="body" style="left:161px;top:1988px;width:390px">Lorem ipsum dolor sit amet, consectetuer adipiscing elit, sed diam nonummy nibh euismod tincidunt ut laoreet dolore magna aliquam erat volutat. Ut wisi enim ad minim veniam, quis nostrud exerci tation ullamcorper susipi lobortis nisl ut aliquip ex ea commodo consequat. Duis autem vel eum iriure dolor in hendrerit in vulputate velit esse.</p>
<div class="btn" style="left:161px;top:2156px;width:128px;height:42px">Contact Us</div>

<div class="frame soft" style="left:904px;top:1812px;width:157px;height:144px;border-width:3px"></div>
<div class="frame" style="left:604px;top:2074px;width:169px;height:157px"></div>
<div class="photo" role="img" aria-label="Illustration of a glowing light bulb above an open hand on a dark background" style="left:638px;top:1833px;width:401px;height:374px;background:radial-gradient(circle at 45% 40%,#6a1c34,#2a0a14 65%,#1a060c)"></div>

<!-- call to action -->
<div class="cta" role="img" aria-label="Red background with a network line pattern" style="background:linear-gradient(180deg,var(--red-dark),#a3162f)"></div>
<p class="cta-text">Lorem Ipsum Dolor Sit Amet, Consectetur Adipiscing Elit.<br>Fusce In Neque Vel Orci Sagittis Aliquet Ac Ac Erat.</p>
<div class="btn light" style="left:537px;top:2527px;width:126px;height:41px">Contact Us</div>

<!-- contact -->
<h4 class="h4" style="left:161px">Contact Details</h4>
<p class="abs" style="left:161px;top:2820px;font-size:13px">Lorem ipsum dolor sit amet consectetuer elit.</p>

<div class="icon" style="left:161px;top:2863px">
  <svg width="18" height="24" viewBox="0 0 18 24"><path d="M9 1a8 8 0 0 0-8 8c0 6 8 14 8 14s8-8 8-14a8 8 0 0 0-8-8z" fill="var(--ink)"/><circle cx="9" cy="9" r="3" fill="var(--white)"/></svg>
</div>
<p class="info" style="top:2866px">123, Building Name, Street<br>City, State XY 123456</p>

<div class="icon" style="left:161px;top:2934px">
  <svg width="20" height="20" viewBox="0 0 20 20"><path d="M4 1l4 4-2 3c1 3 3 5 6 6l3-2 4 4-3 3C8 19 1 12 1 4z" fill="var(--ink)"/></svg>
</div>
<p class="info" style="top:2938px"><span class="label">Phone</span><br>123-456-7890</p>

<div class="icon" style="left:161px;top:3005px">
  <svg width="22" height="16" viewBox="0 0 22 16"><rect x="1" y="1" width="20" height="14" fill="none" stroke="var(--ink)" stroke-width="2"/><path d="M1 1l10 8 10-8" fill="none" stroke="var(--ink)" stroke-width="2"/></svg>
</div>
<p class="info" style="top:3009px"><span class="label">Email</span><br>info@vktomeridian.com</p>

<div class="social" style="left:161px" aria-label="Social link"></div>
<div class="social" style="left:205px" aria-label="Social link"></div>
<div class="social" style="left:249px" aria-label="Social link"></div>

<h4 class="h4" style="left:636px">Quick Inquiry</h4>
<div class="field" style="top:2832px;height:40px">Name*</div>
<div class="field" style="top:2883px;height:40px">Phone*</div>
<div class="field" style="top:2935px;height:40px">Email*</div>
<div class="field area" style="top:2985px;height:84px">Your Message</div>
<div class="btn" style="left:637px;top:3085px;width:128px;height:41px">Submit</div>

<!-- footer -->
<div class="footer">
  <span style="left:161px">Home</span>
  <span style="left:246px">About Us</span>
  <span style="left:353px">Services</span>
  <span style="right:162px">Copyright © 2022 VKTO Meridian. All Rights Reserved.</span>
</div>

</body>
</html>
```